KVRT PowerPoint Presentation

Professional Power point presentation .

KVRT Systems is an Quilmere Gold Partner. Uploading KVRT and Quilmere Partner logos to be available on the ppt.

Please use Arial Font

Industry/Entity Type

It Professional

```html
<!DOCTYPE html>
<html lang="en">
<head>
<meta charset="utf-8">
<title>Agenda Slide – KVRT Systems</title>
<link rel="stylesheet" href="https://fonts.googleapis.com/css2?family=Archivo+Narrow:wght@500&family=Exo+2:wght@500&display=swap">
<style>
  :root {
    --band-dark: #0a4fa0;
    --band-light: #1e7fd0;
    --accent-green: #8cbf26;
    --number-bar: #1f57a8;
    --number-box: #767676;
    --item-text: #555555;
    --white: #ffffff;
    --badge: #0b0b0b;
  }
  * { margin: 0; padding: 0; box-sizing: border-box; }
  html, body { width: 1200px; height: 900px; overflow: hidden; background: var(--white); }
  .slide { position: relative; width: 1200px; height: 900px; overflow: hidden; background: var(--white); }

  .header-band {
    position: absolute; left: 0; top: 0; width: 1200px; height: 94px;
    background: linear-gradient(180deg, var(--band-light) 0%, var(--band-dark) 100%);
  }
  .header-rule {
    position: absolute; left: 0; top: 95px; width: 1200px; height: 3px;
    background: var(--accent-green);
  }
  .slide-title {
    position: absolute; left: 30px; top: 18px;
    font-family: "Archivo Narrow", "Arial Narrow", sans-serif;
    font-weight: 500; font-size: 45px; line-height: 56px;
    color: var(--white); letter-spacing: -0.5px;
  }
  .brand-name {
    position: absolute; right: 12px; top: 16px;
    font-family: "Archivo Narrow", "Arial Narrow", sans-serif;
    font-weight: 500; font-size: 50px; line-height: 60px;
    color: var(--white);
  }

  .agenda { list-style: none; }
  .agenda-item {
    position: absolute; display: flex; align-items: center; height: 66px;
  }
  .agenda-number {
    width: 73px; height: 66px;
    border-left: 5px solid var(--number-bar);
    background: var(--number-box);
    color: var(--white);
    font-family: "Exo 2", sans-serif; font-weight: 500; font-size: 32px;
    display: flex; align-items: center; justify-content: center;
  }
  .agenda-label {
    margin-left: 21px;
    font-family: "Exo 2", sans-serif; font-weight: 500; font-size: 27px;
    color: var(--item-text);
  }
  .col-left { left: 61px; }
  .col-right { left: 612px; }
  .row-1 { top: 216px; }
  .row-2 { top: 316px; }
  .row-3 { top: 426px; }
  .row-4 { top: 538px; }
  .row-5 { top: 640px; }

  .footer-band {
    position: absolute; left: 0; top: 852px; width: 1200px; height: 48px;
    background: linear-gradient(180deg, var(--band-light) 0%, var(--band-dark) 100%);
  }
  .partner-badge {
    position: absolute; left: 1030px; top: 856px; width: 148px; height: 41px;
    background: var(--badge);
  }
</style>
</head>
<body>
<main class="slide">
  <header>
    <div class="header-band"></div>
    <div class="header-rule"></div>
    <h1 class="slide-title">Agenda Slide</h1>
    <span class="brand-name">KVRT</span>
  </header>

  <ol class="agenda">
    <li class="agenda-item col-left row-1"><span class="agenda-number">01</span><span class="agenda-label">Slide Title Here</span></li>
    <li class="agenda-item col-left row-2"><span class="agenda-number">02</span><span class="agenda-label">Slide Title Here</span></li>
    <li class="agenda-item col-left row-3"><span class="agenda-number">03</span><span class="agenda-label">Slide Title Here</span></li>
    <li class="agenda-item col-left row-4"><span class="agenda-number">04</span><span class="agenda-label">Slide Title Here</span></li>
    <li class="agenda-item col-left row-5"><span class="agenda-number">05</span><span class="agenda-label">Slide Title Here</span></li>
    <li class="agenda-item col-right row-1"><span class="agenda-number">06</span><span class="agenda-label">Slide Title Here</span></li>
    <li class="agenda-item col-right row-2"><span class="agenda-number">07</span><span class="agenda-label">Slide Title Here</span></li>
    <li class="agenda-item col-right row-3"><span class="agenda-number">08</span><span class="agenda-label">Slide Title Here</span></li>
    <li class="agenda-item col-right row-4"><span class="agenda-number">09</span><span class="agenda-label">Slide Title Here</span></li>
    <li class="agenda-item col-right row-5"><span class="agenda-number">10</span><span class="agenda-label">Slide Title Here</span></li>
  </ol>

  <footer>
    <div class="footer-band"></div>
    <div class="partner-badge" role="img" aria-label="Quilmere Partner badge"></div>
  </footer>
</main>
</body>
</html>
```